Digital Agency Needs a Relaunch

We are looking for a modern, top-notch design to elevate our brand to win new clients. It has to build on the clarity of message in the current wireframes and must fit together well on Wordpress.

The winning designer will need to complete the other pages, but please focus on the homepage as the base of your proposed designs for us.

Use the existing logo as a point, and the colour scheme should be around that, we currently use these colours, but you can suggest new mixes:
Purple: #5c306b
Orange: #e27927
Grey: #5f4f61
Light grey: #cacaca
Off white: #ececec
Blue: #674ea7
Updates

Target Market(s)

Decent Sized SME Businesses (20+ Staff, Over £1m turnover)

Industry/Entity Type

Digital Marketing

Number of Pages Required

5+ page

Font styles to use
Sans Serif

Colors

Designer to choose colors to be used in the design.

Requirements
Must have
• A real attention on the design piece. Ignore the current website and really focus on the messaging and the brief.
Nice to have
• Read the messages and think about the impact. Use the purple in the logo more than the orange, but try to keep it smart rather than cool
Should not have
• Inconsistent design, serif fonts, stock images and not meeting the wireframes.

```html
<!DOCTYPE html>
<html lang="en">
<head>
<meta charset="utf-8">
<title>Vanta Digital — Growth Works For You</title>
<link href="https://fonts.googleapis.com/css2?family=Raleway:wght@400;500;600;700;800&display=swap" rel="stylesheet">
<style>
:root{
  --night:#231538;
  --night-deep:#1b1030;
  --purple:#5c306b;
  --purple-ink:#3d2458;
  --orange:#f06a22;
  --grey:#5f4f61;
  --light-grey:#cacaca;
  --off-white:#ececec;
  --paper:#f7f7f7;
  --white:#ffffff;
  --lavender:#f0eef7;
}
*{box-sizing:border-box;margin:0;padding:0}
html,body{width:1200px;height:4259px;overflow:hidden}
body{position:relative;font-family:"Raleway",sans-serif;color:var(--grey);background:var(--white)}
.abs{position:absolute}
a{color:inherit;text-decoration:none}

/* hero */
.hero{position:absolute;left:0;top:0;width:1200px;height:1934px;background:radial-gradient(ellipse at 50% 20%,#3a2460 0%,var(--night) 55%,var(--night-deep) 100%)}
.topbar{position:absolute;left:694px;top:0;width:506px;height:24px;background:rgba(255,255,255,.06);border-bottom-left-radius:14px;display:flex;gap:10px;justify-content:center;align-items:center;font-size:10px;color:var(--orange)}
.topbar span.sep{color:#fff;opacity:.6}
.brand{position:absolute;left:205px;top:26px;display:flex;align-items:center;gap:10px;color:#fff;font-weight:700;font-size:30px;letter-spacing:.5px}
.brand .dot{width:16px;height:16px;border-radius:50%;background:#fff}
.brand small{display:block;font-size:11px;font-weight:500;letter-spacing:5px}
.nav{position:absolute;left:607px;top:56px;display:flex;gap:26px;color:#fff;font-size:13px;font-weight:600}
.hero-title{position:absolute;left:0;top:160px;width:1200px;text-align:center;font-weight:800;font-size:46px;line-height:50px;color:#fff;letter-spacing:1px}
.hero-title em{font-style:normal;color:var(--orange);display:block}
.hero-art{position:absolute;left:180px;top:270px;width:840px;height:330px;border-radius:40px;background:radial-gradient(ellipse at 50% 55%,rgba(120,90,170,.35) 0%,rgba(60,36,96,.15) 55%,rgba(35,21,56,0) 80%)}

/* intro */
.intro-text{position:absolute;left:0;width:1200px;text-align:center}
.intro-h{top:672px;font-size:26px;line-height:37px;font-weight:700;color:var(--purple)}
.intro-p{font-size:12.5px;line-height:23px;color:var(--grey)}
.intro-cta{top:1010px;font-size:18px;font-weight:800;color:var(--purple)}
.btn{position:absolute;display:flex;align-items:center;justify-content:center;gap:8px;border-radius:22px;font-size:12px;font-weight:600}
.btn-solid{background:var(--orange);color:#fff}
.btn-line{border:1.5px solid var(--orange);color:var(--orange);background:#fff}

/* services */
.cluster{position:absolute;width:220px;height:220px}
.cluster .band{position:absolute;left:10px;top:88px;width:200px;height:44px;background:#fff;border-radius:22px;text-align:center;line-height:44px;font-weight:800;font-size:18px;color:var(--orange)}
.cluster .node{position:absolute;width:92px;height:92px;border-radius:50%;border:3px solid #fff;background:radial-gradient(circle at 50% 40%,#4a3570 0%,#231538 75%);display:flex;align-items:center;justify-content:center;text-align:center;color:#fff;font-size:10px;font-weight:800;line-height:12px}
.n1{left:17px;top:0}.n2{left:111px;top:0}.n3{left:17px;top:128px}.n4{left:111px;top:128px}

/* pain / gain */
.pg-circle{position:absolute;width:168px;height:168px;border-radius:50%;background:#fff;box-shadow:0 4px 16px rgba(0,0,0,.18);overflow:hidden}
.pg-circle .fill{position:absolute;inset:18px;border-radius:50%}
.pg-line{position:absolute;height:1.5px;background:var(--orange);opacity:.7}
.pg-label{font-size:15px;font-weight:800}
.pg-copy{font-size:11px;line-height:17px;font-style:italic;color:var(--grey)}

/* growth */
.growth-h{left:205px;top:2226px;font-size:19px;font-weight:600;color:var(--purple-ink);white-space:nowrap}
.growth-h b{font-weight:600;color:var(--orange)}
.growth-h i{display:inline-block;vertical-align:-1px;margin-right:6px;width:12px;height:12px;border-radius:50%;border:2px solid var(--orange)}
.growth-p{left:205px;width:312px;font-size:12.5px;line-height:19px;color:var(--grey)}
.growth-p u{color:var(--orange)}
.growth-art{left:549px;top:2185px;width:720px;height:452px;border-radius:226px 0 0 226px;background:var(--lavender)}
.growth-art .fill{position:absolute;left:40px;top:20px;width:440px;height:410px;border-radius:30px;background:linear-gradient(160deg,#f6d5e0 0%,#cfc3ef 50%,#8f77c9 100%);opacity:.75}

/* case studies */
.cases{left:0;top:2711px;width:1200px;height:377px;background:var(--off-white)}
.section-h{font-size:26px;font-weight:800;color:var(--purple-ink);letter-spacing:.5px}
.case{position:absolute;top:89px;height:218px;border-radius:6px;overflow:hidden}
.case .more{position:absolute;left:0;bottom:22px;width:75%;height:24px;background:var(--orange);color:#fff;font-size:12px;font-style:italic;font-weight:600;line-height:24px;padding-left:36px}
.arrow-btn{position:absolute;top:2893px;width:32px;height:32px;border-radius:50%;display:flex;align-items:center;justify-content:center}

/* blog */
.post{position:absolute;top:3255px;width:240px;height:249px;background:#f3f3f3;box-shadow:0 3px 10px rgba(0,0,0,.12);border-radius:4px;overflow:hidden}
.post .pic{position:absolute;left:0;top:0;width:100%;height:158px}
.post .tag{position:absolute;left:0;top:140px;height:28px;padding:0 18px;background:var(--purple-ink);color:#fff;font-size:10px;line-height:28px;border-radius:0 14px 14px 0}
.post h3{position:absolute;left:18px;top:182px;width:200px;font-size:11px;line-height:16px;font-weight:500;color:var(--purple-ink)}
.post .read{position:absolute;left:18px;top:229px;font-size:9px;font-weight:800;color:var(--orange);letter-spacing:.5px}
.turbo{left:286px;top:3671px;width:626px;height:65px;border:1.5px solid var(--purple);border-radius:33px;background:#fff;z-index:3}
.turbo p{position:absolute;left:48px;top:0;line-height:62px;font-size:12px;color:var(--grey)}
.turbo i{position:absolute;left:22px;top:25px;width:14px;height:14px;border-radius:50%;border:2px solid var(--purple)}

/* footer */
.footer{left:0;top:3700px;width:1200px;height:559px;background:var(--night)}
.fcol{position:absolute;color:#fff;font-size:12px;font-weight:500}
.fcol h4{color:var(--orange);font-size:14px;font-weight:500;margin-bottom:8px;letter-spacing:.5px}
.fcol li{list-style:none;line-height:22px}
.fcol li::before{content:"• "}
.fcol p{line-height:23px}
.legal{position:absolute;top:4224px;font-size:9px;color:#fff}
</style>
</head>
<body>

<section class="hero">
  <div class="topbar"><span>Blog</span><span class="sep">|</span><span>About Us</span><span class="sep">|</span><span>Contact Us</span><span class="sep">|</span><span>01 234 567 890</span></div>
  <div class="brand"><span class="dot"></span><div>Vanta<small>DIGITAL</small></div></div>
  <nav class="nav"><a>Create</a><a>Communicate</a><a>Convert</a><a>Close</a><a>Case Studies</a></nav>
  <h1 class="hero-title">GROWTH WORKS<em>FOR YOU</em></h1>

  <div class="hero-art" role="img" aria-label="Illustration of a rocket launching among clouds"></div>

  <!-- services -->
  <div class="cluster" style="left:343px;top:1254px">
    <div class="band">CREATE</div>
    <div class="node n1">BRANDING</div><div class="node n2">GRAPHICS</div><div class="node n3">VIDEO</div><div class="node n4">CONTENT</div>
  </div>
  <div class="cluster" style="left:632px;top:1254px">
    <div class="band">COMMUNICATE</div>
    <div class="node n1">ADS</div><div class="node n2">ORGANIC</div><div class="node n3">SOCIAL</div><div class="node n4">EMAIL</div>
  </div>
  <div class="cluster" style="left:343px;top:1555px">
    <div class="band">CONVERT</div>
    <div class="node n1">WEBSITES</div><div class="node n2">LEAD<br>GENERATION</div><div class="node n3">E-COMMERCE</div><div class="node n4">ANALYTICS</div>
  </div>
  <div class="cluster" style="left:632px;top:1555px">
    <div class="band">CLOSE</div>
    <div class="node n1">CRM</div><div class="node n2">SYSTEMS</div><div class="node n3">CUSTOMER<br>SUCCESS</div><div class="node n4">AI &amp;<br>AUTOMATIONS</div>
  </div>
</section>

<svg class="abs" style="left:0;top:0" width="1200" height="4259" viewBox="0 0 1200 4259">
  <path d="M0 678 Q600 496 1200 678 L1200 1090 Q600 1190 0 1090 Z" fill="#f7f7f7"/>
  <path d="M0 1934 Q600 1752 1200 1934 L1200 2711 L0 2711 Z" fill="#ffffff"/>
</svg>

<!-- intro -->
<h2 class="abs intro-text intro-h">Fed up with agencies who don’t care?<br>We’ve heard that before</h2>
<p class="abs intro-text intro-p" style="top:765px">We know every client has unique needs. Yet, few digital agencies<br>spend enough time getting to know the client’s business.</p>
<p class="abs intro-text intro-p" style="top:833px">We’re different. We take a highly personalised approach to every<br>project, working closely with our clients to understand their<br>objectives, challenges, and target audience.</p>
<p class="abs intro-text intro-p" style="top:922px">Knowing your business is the first step in helping you grow. It’s how<br>we work, and it will work for you.</p>
<h3 class="abs intro-text intro-cta">ACHIEVE GROWTH THAT WORKS</h3>
<a class="btn btn-solid" style="left:514px;top:1053px;width:172px;height:40px">Set Up A Call
  <svg width="16" height="16" viewBox="0 0 16 16"><path d="M3 13l3-3M6 13l9-12-12 9 3 0z" fill="none" stroke="#fff" stroke-width="1.3"/></svg></a>

<!-- pain / gain -->
<div class="pg-line" style="left:330px;top:1936px;width:540px"></div>
<div class="pg-line" style="left:330px;top:2058px;width:540px"></div>
<div class="pg-circle" style="left:184px;top:1911px"><div class="fill" role="img" aria-label="Illustration of a developer stressed at a desk" style="background:linear-gradient(160deg,#eef1fb,#c9d3f3)"></div></div>
<div class="pg-circle" style="left:846px;top:1911px"><div class="fill" role="img" aria-label="Illustration of a team celebrating revenue growth" style="background:linear-gradient(160deg,#f3eefb,#d9cdf0)"></div></div>
<div class="abs" style="left:366px;top:1958px;color:var(--purple-ink)"><div class="pg-label">YOUR PAIN?</div><p class="pg-copy" style="margin-top:6px">“I spend most of my development<br>budget fixing errors and bugs”</p></div>
<svg class="abs" style="left:583px;top:1979px" width="34" height="34" viewBox="0 0 34 34"><circle cx="17" cy="17" r="16" fill="#fff" stroke="#e0e0e0"/><path d="M13 10l10 7-10 7z" fill="none" stroke="#f06a22" stroke-width="2"/></svg>
<div class="abs" style="left:647px;top:1956px"><div class="pg-label" style="color:var(--orange)">FUTURE GAIN</div><p class="pg-copy" style="margin-top:6px">A fast &amp; reliable cash-generative<br>content-managed e-commerce<br>or lead generation website</p></div>
<a class="btn btn-solid" style="left:646px;top:2046px;width:113px;height:25px;font-size:10px">Websites</a>

<!-- growth -->
<div class="abs growth-art"><div class="fill" role="img" aria-label="Illustration of a rocket above a phone with people building a marketing dashboard"></div></div>
<h2 class="abs growth-h"><i></i>VANTA: WHERE <b>GROWTH</b> WORKS</h2>
<p class="abs growth-p" style="top:2262px">We understand the importance of a strong online presence. That’s why we offer a complete range of digital marketing solutions to help you reach your growth goals.</p>
<p class="abs growth-p" style="top:2356px">Our <u>track record</u> demonstrates expertise in all forms of digital marketing, including <u>Website builds</u>, <u>Search Ads</u>, <u>SEO</u>, <u>Email Marketing</u>.</p>
<p class="abs growth-p" style="top:2431px">We’re constantly staying up-to-date on the latest trends, tech and best practices in the industry, so you can trust that you’re getting the most effective and efficient strategies for your business growth.</p>
<p class="abs growth-p" style="top:2525px">Set up a call and we’re confident we can show you where we can add growth and value to your business.</p>

<!-- case studies -->
<section class="abs cases">
  <h2 class="abs section-h" style="left:205px;top:32px">CREATE <span style="color:var(--orange);font-size:18px">→</span> CASE STUDIES</h2>
  <div class="case" role="img" aria-label="Photo of an electric car charging" style="left:0;width:190px;background:linear-gradient(135deg,#0f3f6e,#2b8ad6 55%,#0b1d33)"></div>
  <div class="case" style="left:205px;width:188px;background:linear-gradient(160deg,#6d8aa6,#2a3c52 60%,#a53a3a)" role="img" aria-label="Photo of trading screens with charts"><span class="more">LEARN MORE</span></div>
  <div class="case" style="left:407px;width:186px;background:linear-gradient(180deg,#f6f6f6 0%,#e4ebef 100%)" role="img" aria-label="Screenshot of an analytics dashboard"><span class="more">LEARN MORE</span></div>
  <div class="case" style="left:607px;width:186px;background:linear-gradient(150deg,#d9822e,#5b3a28 55%,#1c1f2b)" role="img" aria-label="Photo of a hand using a shopping app on a phone"><span class="more">LEARN MORE</span></div>
</section>
<div class="arrow-btn" style="left:835px;border:1.5px solid #bdbdbd"><svg width="10" height="12" viewBox="0 0 10 12"><path d="M7 1L2 6l5 5" fill="none" stroke="#bdbdbd" stroke-width="1.5"/></svg></div>
<div class="arrow-btn" style="left:890px;border:1.5px solid var(--orange)"><svg width="10" height="12" viewBox="0 0 10 12"><path d="M3 1l5 5-5 5" fill="none" stroke="#f06a22" stroke-width="1.5"/></svg></div>

<!-- blog -->
<h2 class="abs section-h" style="left:0;top:3180px;width:1200px;text-align:center">FROM THE BLOG</h2>
<article class="post" style="left:205px"><div class="pic" role="img" aria-label="Photo of a team planning around a table" style="background:linear-gradient(135deg,#cfcfcf,#7a7a80)"></div><span class="tag">Tech</span><h3>Searchly’s New PPC Features are Loaded with AI</h3><span class="read">READ MORE</span></article>
<article class="post" style="left:481px"><div class="pic" role="img" aria-label="Photo of app icons on a phone screen" style="background:linear-gradient(135deg,#9a1c2a,#d43b3b 55%,#2b7bd1)"></div><span class="tag">Tech</span><h3>How Searchly Killed the Broad Match Keyword?</h3><span class="read">READ MORE</span></article>
<article class="post" style="left:754px"><div class="pic" role="img" aria-label="Photo of a person working at a laptop" style="background:linear-gradient(135deg,#d8dde3,#3b4250)"></div><span class="tag">Social Media</span><h3>The 9 Rules of Social Media Engagement (Part II)</h3><span class="read">READ MORE</span></article>
<a class="btn btn-line" style="left:514px;top:3554px;width:172px;height:40px">Visit Blog</a>

<!-- footer -->
<footer class="abs footer">
  <svg class="abs" style="left:0;top:0" width="1200" height="100" viewBox="0 0 1200 100"><path d="M0 0 H1200 V20 Q600 160 0 20 Z" fill="#ffffff"/></svg>
  <div class="fcol" style="left:205px;top:190px"><h4>CREATE</h4><ul><li>Branding</li><li>Graphics</li><li>Video</li><li>Content</li></ul></div>
  <div class="fcol" style="left:205px;top:342px"><h4>COMMUNICATE</h4><ul><li>Ads</li><li>Organic</li><li>Social</li><li>Email</li></ul></div>
  <div class="fcol" style="left:430px;top:190px"><h4>CONVERT</h4><ul><li>Websites</li><li>Lead Generation</li><li>E-commerce</li><li>Analytics</li></ul></div>
  <div class="fcol" style="left:430px;top:342px"><h4>CLOSE</h4><ul><li>CRM</li><li>Systems</li><li>Customer Success</li><li>AI &amp; Automations</li></ul></div>
  <div class="fcol" style="left:641px;top:190px"><h4>CONNECT</h4><ul><li>Case Studies</li><li>Blog</li><li>About Us</li></ul></div>
  <div class="fcol" style="left:855px;top:190px"><h4>CONTACT</h4><ul><li>Contact Us</li><li>Tel: <u>01 234 567 890</u></li></ul></div>
  <div class="fcol" style="left:855px;top:334px"><h4>ADDRESS</h4><p>Harbour Point House,<br>Elmford, Westshire<br>EF1 2AB</p></div>
</footer>
<div class="abs turbo"><i></i><p>We’re the turbo boost for your digital marketing engine</p>
  <a class="btn btn-solid" style="left:436px;top:13px;width:176px;height:38px">Put Your Foot Down</a></div>
<span class="legal" style="left:205px">Vanta Digital Limited. All Rights Reserved</span>
<span class="legal" style="left:768px;width:225px;text-align:right">Sitemap | Terms of Use | Privacy | Policy</span>

</body>
</html>
```